Mailchimp Template Design

We are looking to create two types of email template for use specifically within Mailchimp including a Newsletter Template Layout and a Campaign Template Layout, as such require the templates to be designed in HTML to be compatible with Mailchimp.

The Newsletter Template Layout should accommodate for three newsletter article features and two separate product offer features. Each newsletter article feature should contain: A small image (16:9 ratio), a Feature title and up to 100 words as a short description and each Product offer feature should show a large image (4:3 ratio) and short description of

The Campaign Template Layout should accommodate for one large (4:3 ratio) campaign image, a small description of 50 words and three product offer areas.

The look and feel of the designs should be consistent with the Brisk Lane website (www.brisklane.co.uk) and the uploaded source material that is attached to this project brief.
Updates

Reason: Review of other business marketing efforts to see which design is the most contextually relevant.

Target Market(s)

Pet Owning Consumer

Industry/Entity Type

Pet Shop

Number of Pages Required

2 page

Other font styles liked:
• Provided in Brief Attachment

Requirements
Must have
• Compatibility with Mail Chimp
• Consistency with Brisk Lane (www.brisklane.co.uk) Look & Feel and Brand Guidelines

```html
<!DOCTYPE html>
<html lang="en">
<head>
<meta charset="utf-8">
<title>Brisk Lane – Newsletter</title>
<link href="https://fonts.googleapis.com/css2?family=Fredoka:wght@600&family=Open+Sans:wght@400;600;700&family=Quicksand:wght@500&display=swap" rel="stylesheet">
<style>
:root{
  --sky:#3aa8de;
  --ocean:#2a86bd;
  --footer:#2784b8;
  --mist:#eeeeee;
  --olive:#6e7a2a;
  --plum:#834a76;
  --aqua:#55c1ec;
  --ink:#333333;
  --muted:#555555;
  --sale:#d60000;
  --white:#ffffff;
}
*{margin:0;padding:0;box-sizing:border-box}
html,body{width:1200px;height:1200px;overflow:hidden;background:var(--white)}
body{font-family:"Open Sans",Arial,sans-serif;color:var(--ink)}
.email{position:absolute;left:424px;top:16px;width:440px;height:1458px;transform:scale(0.8);transform-origin:0 0}
.topbar{position:absolute;left:0;top:0;width:440px;height:37px;background:var(--sky);display:flex;align-items:center;padding:0 22px;color:var(--white)}
.brand{display:flex;align-items:center;gap:5px;font-weight:700;font-size:12px;width:112px}
.brand-dot{width:8px;height:8px;border-radius:50%;background:var(--white)}
.contact{font-size:10.5px;display:flex;align-items:center;gap:4px}
.contact svg{width:9px;height:9px;fill:var(--white)}
.hero-head{position:absolute;left:0;top:37px;width:440px;height:52px;background:var(--ocean);color:var(--white);text-align:center}
.hero-head h1{font-family:"Fredoka",sans-serif;font-weight:600;font-size:23px;letter-spacing:.3px;line-height:1;padding-top:7px}
.hero-sub{display:flex;align-items:center;justify-content:center;gap:8px;font-size:14px;font-weight:400;margin-top:2px}
.hero-sub i{display:block;width:70px;height:2px;background:var(--white)}
.promo{position:absolute;left:0;top:103px;width:440px;height:175px;background:var(--mist)}
.promo-photo{position:absolute;left:22px;top:16px;width:238px;height:137px;border-radius:3px;background:linear-gradient(120deg,#5e8a35 0%,#a7b36a 45%,#d9b48a 75%,#c9a37a 100%)}
.promo-card{position:absolute;left:271px;top:16px;width:147px;height:137px;background:var(--olive);color:var(--white);padding:9px 8px;overflow:hidden}
.promo-card h3{font-size:11px;font-weight:700;line-height:16px;margin-bottom:5px}
.promo-card p{font-size:8.5px;line-height:15.5px}
.promo-fish{position:absolute;right:0;bottom:-2px;width:66px;height:56px;border-radius:50% 40% 40% 50%;background:radial-gradient(circle at 40% 50%,#f9a31a,#e87f0c)}
.ribbon{position:absolute;height:21px;border-radius:11px 4px 11px 4px;color:var(--white);font-family:"Quicksand",sans-serif;font-weight:500;text-align:center;letter-spacing:1px;line-height:21px}
.ribbon-articles{left:80px;top:298px;width:292px;background:var(--sky);font-size:19px}
.ribbon-offers{left:67px;top:1042px;width:303px;background:var(--footer);font-size:19px;line-height:23px;height:23px}
.article{position:absolute;top:341px;width:195px;height:593px;color:var(--white);padding:19px 7px 0}
.article-plum{left:22px;background:var(--plum)}
.article-aqua{left:223px;background:var(--aqua)}
.article h2{font-size:11px;font-weight:700;margin-bottom:4px}
.article p{font-size:8.5px;line-height:15.5px}
.article ul{list-style:none;font-size:11.5px;line-height:13.5px;margin:8px 0}
.article li{padding-left:10px;text-indent:-10px;margin-bottom:12px}
.article li::before{content:"• "}
.article-aqua ul{margin:14px 0 6px}
.article-aqua li{padding-left:8px;text-indent:-8px}
.bird{position:absolute;left:142px;top:860px;width:106px;height:152px;border-radius:45% 45% 20% 20%;background:linear-gradient(180deg,#f2e36a 0%,#b9b9b9 35%,#8d8d8d 100%)}
.hedgehog{position:absolute;left:303px;top:880px;width:117px;height:95px;border-radius:55% 50% 40% 40%;background:radial-gradient(circle at 40% 60%,#d9d0c6 0%,#5a5a5a 55%,#2b2b2b 100%)}
.pup{position:absolute;left:350px;top:1028px;width:45px;height:52px;border-radius:40%;background:linear-gradient(180deg,#e7c9a0,#3c9a3a)}
.offers{position:absolute;left:22px;top:1090px;width:400px;display:flex;gap:6px}
.offer{width:128px}
.offer-art{height:125px;margin-bottom:9px;border-radius:40%}
.art-cat{background:radial-gradient(ellipse at 50% 55%,#f3b77a 0%,#f6e7d6 55%,transparent 72%)}
.art-cavy{background:radial-gradient(ellipse at 50% 60%,#e59a2f 0%,#f3d9b4 55%,transparent 72%)}
.art-fish{background:radial-gradient(ellipse at 50% 50%,#f9a31a 0%,#f6c36a 50%,transparent 72%)}
.offer h3{font-size:11px;font-weight:700;line-height:16px;color:var(--ink);margin-bottom:6px}
.offer p{font-size:8.5px;line-height:15.5px;color:var(--muted)}
.offer ul{list-style:none;font-size:11px;line-height:13px;margin:17px 0 8px;color:var(--ink)}
.offer li::before{content:"•  "}
.price{font-size:11px;color:var(--muted)}
.price s{font-size:8.5px}
.price strong{font-size:14px;color:var(--sale);font-weight:700}
.footer{position:absolute;left:0;top:1416px;width:440px;height:42px;background:var(--footer);color:var(--white);font-size:8.5px;font-weight:600;text-align:center;line-height:42px}
</style>
</head>
<body>
<div class="email">
  <header class="topbar">
    <div class="brand"><span class="brand-dot"></span>Brisk Lane</div>
    <div class="contact">
      <svg viewBox="0 0 10 10"><path d="M2 0.5 3.6 2.4 2.8 3.6C3.4 5 4.9 6.5 6.4 7.2L7.6 6.4 9.5 8 8.7 9.5C4.5 9.2 0.8 5.5 0.5 1.3Z"/></svg>
      01632 960418 (Mon-Fri) |
      <svg viewBox="0 0 10 10"><path d="M0.5 2h9v6h-9zM1 2.5 5 5.5 9 2.5" stroke="#3aa8de" stroke-width=".8"/></svg>
      customerservices@brisklane.co.uk
    </div>
  </header>
  <section class="hero-head">
    <h1>IT'S DELICIOUS AND HEALTHY TOO!</h1>
    <div class="hero-sub"><i></i>grab the best food for your dog now!<i></i></div>
  </section>

  <section class="promo">
    <div class="promo-photo" role="img" aria-label="Puppy on grass behind three tins of dog food with a free tin offer seal"></div>
    <div class="promo-card">
      <h3>Lorem ipsum dolor sit amet</h3>
      <p>Lorem ipsum dolor sit amet, consectetur adipiscing elit. Cras eu ex eros. Fusce tristique tincidunt nulla sed commodo.</p>
      <div class="promo-fish" role="img" aria-label="Cartoon goldfish"></div>
    </div>
  </section>

  <div class="ribbon ribbon-articles">ARTICLES FOR YOU</div>

  <article class="article article-plum">
    <h2>Lorem ipsum dolor sit amet</h2>
    <p>Lorem ipsum dolor sit amet, consectetur adipiscing elit. Cras eu ex eros. Fusce tristique tincidunt nulla sed commodo.</p>
    <ul>
      <li>Nam quam magna,pretium eget tortor ut, vulputate erat.</li>
      <li>Morbi nec blandit nisi. Cras cursus cursu lacinia. Donec quis lobortis lorem.</li>
    </ul>
    <p>Duis odio nulla, commodo vel vestibulum quis, consectetur et risus. Quisque nisl lacus, tristique ut sodales a, blandit vitae elit.</p>
    <ul>
      <li>Phasellus cursus commodo nibh, a congue dolor rhoncus id.</li>
    </ul>
    <p>Duis elementum blandit turpis vel faucibus. Quisque ut arcu elementum, tincidunt quam viverra, malesuada mauris. Duis vel diam ac metus lobortis commodo nec vitae lorem. Duis vel vehicula sem. Etiam nec blandit eros, ut mollis velit. Nullam dapibus eros ut ex maximus pretium. Sed malesuada pellentesque consequat. Nunc in orci egestas, ultrices est ut, commodo lorem. Fusce imperdiet hendrerit purus. Class aptent taciti sociosqu ad litora torquent per conubia nostra, per inceptos himenaeos.</p>
  </article>

  <article class="article article-aqua">
    <h2>Lorem ipsum dolor sit amet</h2>
    <p>Lorem ipsum dolor sit amet, consectetur adipiscing elit. Cras eu ex eros. Fusce tristique tincidunt nulla sed commodo. Nam quam magna, pretium eget tortor ut, vulputate erat. Morbi nec blandit nisi. Cras cursus cursu lacinia.<br>Donec quis lobortis lorem.</p>
    <p style="margin-top:3px">Duis odio nulla, commodo vel vestibulum quis, consectetur et risus.</p>
    <ul>
      <li>Quisque nisl lacus, tristique ut sodales a, blandit vitae elit. Phasellus cursus commodo nibh, a congue dolor rhoncus id. Etiam tristique ante quis porta ornare.</li>
    </ul>
    <p>Duis elementum blandit turpis vel faucibus. Quisque ut arcu elementum, tincidunt quam viverra, malesuada mauris. Duis vel diam ac metus lobortis commodo nec vitae lorem.Duis vel vehicula sem. Etiam nec blandit eros, ut mollis velit. Nullam dapibus eros ut ex maximus pretium. Sed malesuada pellentesque consequat. Nunc in orci egestas, ultrices est ut, commodo lorem. Fusce imperdiet hendrerit purus. Class aptent taciti sociosqu ad litora torquent per conubia nostra, per inceptos himenaeos. Praesent non consectetur dui. Duis orci magna, dictum quis nibh a, placerat posuere enim. Etiam bibendum lorem quis justo malesuada vestibulum.</p>
  </article>

  <div class="bird" role="img" aria-label="Cartoon cockatiel perched on a branch"></div>
  <div class="hedgehog" role="img" aria-label="Cartoon hedgehog"></div>

  <div class="ribbon ribbon-offers">BEST PRODUCT OFFERS</div>
  <div class="pup" role="img" aria-label="Cartoon puppy in a festive scarf"></div>

  <section class="offers">
    <div class="offer">
      <div class="offer-art art-cat" role="img" aria-label="Cartoon calico cat"></div>
      <h3>Lorem ipsum dolor sit amet</h3>
      <p>Lorem ipsum dolor sit amet, consectetur adipiscing elit. Cras eu ex eros. Fusce tristique tincidunt nulla sed commodo.</p>
      <ul><li>Nam quam magna, pretium eget tortor ut, vulputate erat.</li></ul>
      <div class="price">Price: <s>123.00</s> <strong>95.00</strong></div>
    </div>
    <div class="offer">
      <div class="offer-art art-cavy" role="img" aria-label="Cartoon guinea pig"></div>
      <h3>Lorem ipsum dolor sit amet</h3>
      <p>Lorem ipsum dolor sit amet, consectetur adipiscing elit. Cras eu ex eros. Fusce tristique tincidunt nulla sed commodo.</p>
      <ul><li>Nam quam magna, pretium eget tortor ut, vulputate erat.</li></ul>
      <div class="price">Price: <s>123.00</s> <strong>95.00</strong></div>
    </div>
    <div class="offer">
      <div class="offer-art art-fish" role="img" aria-label="Cartoon goldfish"></div>
      <h3>Lorem ipsum dolor sit amet</h3>
      <p>Lorem ipsum dolor sit amet, consectetur adipiscing elit. Cras eu ex eros. Fusce tristique tincidunt nulla sed commodo.</p>
      <ul><li>Nam quam magna, pretium eget tortor ut, vulputate erat.</li></ul>
      <div class="price">Price: <s>123.00</s> <strong>95.00</strong></div>
    </div>
  </section>

  <footer class="footer">Copyright © 2017 Brisk Lane Ltd</footer>
</div>
</body>
</html>
```